Look Round Eastvale....a heavily based video and picture gallery style website.

Would like a multipage website for videos and pictures. For example, one page/category will be Events. I would like that page to be a thumbnail gallery where the user would click on a thumbnail and the video will play over/hover the the thumbnail page(not go to another page). So when the user closes the player, they are still on the events page. On each page, would like a navigation bar to be able to go to the other pages/categories. And I would like it this way for the other categories as well (people, places, meet the vendors, pictures....) Please view my current website for all pages needed. I only submitted a fraction of images. How should i send the videos? Please contact if questions.
My current website is at www.lookroundeastvale.net

Target Market(s)

male/female, 30-70+ years old

Industry/Entity Type

Entertainment

Coding

Coded - Design and coding required

Number of Pages Required

5+ page

Font styles to use
Sans Serif

Colors
0393ce
00a990
f04a51
f68d4e

Requirements
Must have
• social media links. the video player must play/hover over the current page rather than going to another page. my logo. a calendar page where I can add events to it. a text area under videos for description, photo gallery for each category, the ability to copy a page to use as a template to add more videos and pictures in the future, contact page, the ability to add google ads, affiliate advertising.

```html
<!DOCTYPE html>
<html lang="en">
<head>
<meta charset="utf-8">
<title>Look Round Eastvale</title>
<link href="https://fonts.googleapis.com/css2?family=Open+Sans:wght@400;600;700&family=Roboto+Condensed:wght@400;700&display=swap" rel="stylesheet">
<style>
:root{
  --blue:#0393ce;
  --teal:#00a990;
  --red:#f04a51;
  --orange:#f68d4e;
  --ink:#1d1d1d;
  --grey:#666;
  --light:#eeeeee;
  --footer:#1c1c1c;
  --deep-teal:#0e7f73;
  --deep-blue:#19729e;
  --badge:#0d6b5e;
}
*{box-sizing:border-box;margin:0;padding:0}
html,body{width:1200px;height:3644px;overflow:hidden}
body{font-family:"Open Sans",Arial,sans-serif;color:var(--ink);background:#fff;position:relative}
a{color:inherit;text-decoration:none}
.heading{font-family:"Roboto Condensed","Arial Narrow",sans-serif;font-weight:400;text-transform:uppercase;text-align:center;font-size:34px;letter-spacing:.5px}

/* header */
.site-header{height:140px;display:flex;align-items:center;padding:0 90px;justify-content:space-between}
.brand{display:flex;align-items:center;gap:12px;color:var(--deep-teal);font-weight:700;font-size:24px;line-height:1}
.brand-dot{width:34px;height:34px;border-radius:50%;background:var(--blue)}
.main-nav{display:flex;align-items:center;gap:0}
.main-nav a{font-size:15px;text-transform:uppercase;color:#333;padding:0 16px}
.main-nav a.active{color:var(--red)}
.search{margin-left:14px;width:190px;height:44px;border:1.5px solid #bbb;border-radius:22px;display:flex;align-items:center;justify-content:space-between;padding:0 16px;color:#888;font-size:14px}

/* hero */
.hero{position:relative;height:560px;overflow:hidden}
.hero-photo{position:absolute;inset:0;background:linear-gradient(100deg,#4b5a44 0%,#7a5a57 30%,#b58f7c 50%,#9aa6a0 70%,#3f5a46 100%)}
.hero-text{position:absolute;top:236px;left:0;right:0;text-align:center;color:#fff}
.hero-text h1{font-family:"Roboto Condensed","Arial Narrow",sans-serif;font-weight:400;font-size:54px;letter-spacing:1px}
.hero-text p{font-family:"Roboto Condensed","Arial Narrow",sans-serif;font-weight:700;font-size:27px;margin-top:2px}
.hero-arrows{position:absolute;left:1048px;top:474px;display:flex;gap:8px}
.hero-arrows span{width:28px;height:28px;border-radius:50%;background:rgba(90,90,90,.8);display:flex;align-items:center;justify-content:center}
.hero-wave{position:absolute;left:0;bottom:0;width:1200px;height:90px}

/* welcome */
.welcome{height:303px;padding-top:87px;text-align:center}
.welcome .heading{font-size:32px}
.welcome p{width:1030px;margin:22px auto 0;font-size:13.5px;line-height:22px;color:#555}

/* category */
.band{position:relative;overflow:hidden}
.band-bg{position:absolute;inset:0}
.category{height:654px}
.category .band-bg{background:radial-gradient(ellipse at 30% 20%,#1d9a89 0%,#0f7f72 55%,#0b6d62 100%)}
.band .heading{position:relative;color:#fff;padding-top:70px}
.category-grid{position:relative;display:grid;grid-template-columns:repeat(4,248px);column-gap:11px;row-gap:28px;margin:46px 0 0 90px}
.category-card{background:#fff}
.thumb{position:relative;display:flex;align-items:center;justify-content:center}
.category-card .thumb{height:143px}
.category-card .label{height:49px;display:flex;align-items:center;justify-content:center;font-size:15px;text-transform:uppercase;color:#444}
.play{width:54px;height:54px}

/* recent */
.recent{height:737px;padding-top:117px}
.recent-grid{display:flex;gap:10px;margin:36px 0 0 90px}
.feature{width:675px;height:420px;box-shadow:0 0 6px rgba(0,0,0,.25);background:#fff}
.feature .thumb{height:330px}
.feature h3{font-weight:600;font-size:20px;margin:18px 0 0 32px}
.feature p{font-size:13px;color:#666;margin:4px 0 0 32px}
.side-list{width:340px;height:424px;box-shadow:0 0 6px rgba(0,0,0,.25);background:#fff;padding:14px 12px 0}
.side-item{display:flex;height:114px;margin-bottom:8px;box-shadow:0 0 4px rgba(0,0,0,.18)}
.side-item .thumb{width:155px;height:114px;flex:none}
.side-item .play{width:46px;height:46px}
.side-info{padding:14px 12px 0 14px}
.side-info h4{font-weight:600;font-size:14px}
.side-info p{font-size:11px;line-height:15px;color:#666;margin-top:8px}
.view-more{display:block;text-align:center;color:var(--red);font-size:12px;margin-top:12px}

/* coming soon */
.coming{height:437px}
.coming .band-bg{background:linear-gradient(180deg,#1f80ad 0%,#17719c 55%,#14618a 100%)}
.coming .heading{padding-top:68px}
.coming-grid{position:relative;display:grid;grid-template-columns:repeat(4,252px);column-gap:6px;margin:34px 0 0 88px}
.coming-card{background:#fff}
.coming-card .thumb{height:140px}
.coming-card .label{height:49px;display:flex;align-items:center;justify-content:center;font-size:17px;color:#333}

/* events */
.events{height:571px;padding-top:91px}
.event-grid{display:grid;grid-template-columns:repeat(3,311px);column-gap:40px;margin:45px 0 0 97px}
.event .thumb{height:175px}
.event-meta{display:flex;margin-top:10px;height:24px}
.event-meta .date{background:var(--badge);color:#fff;font-size:12px;padding:0 12px;display:flex;align-items:center}
.event-meta .count{background:#222;color:#fff;font-size:12px;padding:0 10px;display:flex;align-items:center;gap:4px;margin-left:2px}
.event h3{font-weight:400;font-size:17px;margin-top:14px}
.event p{font-size:12.5px;line-height:17px;color:#777;margin-top:6px}
.event .more{display:block;color:var(--deep-teal);font-size:12.5px;margin-top:6px}

/* footer */
.site-footer{border-top:10px solid var(--orange);background:var(--footer);height:252px;color:#fff;text-align:center;padding-top:68px}
.footer-nav{font-size:12px;text-transform:uppercase}
.footer-nav span{color:#888;margin:0 8px}
.social{display:flex;justify-content:center;gap:9px;margin-top:18px}
.social span{width:26px;height:26px;border-radius:50%;border:1.5px solid #aaa}
.copyright{font-size:12px;margin-top:14px}
</style>
</head>
<body>

<header class="site-header">
  <a class="brand" href="#"><span class="brand-dot"></span>Look Round Eastvale</a>
  <nav class="main-nav">
    <a class="active" href="#">Home</a>
    <a href="#">Videos</a>
    <a href="#">Photo Gallery</a>
    <a href="#">Calendar</a>
    <a href="#">Contact</a>
    <div class="search">Search
      <svg width="14" height="14" viewBox="0 0 14 14"><circle cx="6" cy="6" r="4.5" fill="none" stroke="#555" stroke-width="1.8"/><line x1="9.3" y1="9.3" x2="13" y2="13" stroke="#555" stroke-width="1.8"/></svg>
    </div>
  </nav>
</header>

<section class="hero">
  <div class="hero-photo" role="img" aria-label="Two smiling women at an outdoor market with craft stalls behind them"></div>
  <div class="hero-text">
    <h1>LOOK ROUND EASTVALE</h1>
    <p>Neque porro quisquam dolorem ipsum</p>
  </div>
  <div class="hero-arrows">
    <span><svg width="10" height="12" viewBox="0 0 10 12"><path d="M7 1L2 6l5 5" fill="none" stroke="#fff" stroke-width="2"/></svg></span>
    <span><svg width="10" height="12" viewBox="0 0 10 12"><path d="M3 1l5 5-5 5" fill="none" stroke="#fff" stroke-width="2"/></svg></span>
  </div>
  <svg class="hero-wave" viewBox="0 0 1200 90" preserveAspectRatio="none">
    <path d="M0 30 Q300 110 620 55 T1200 8 L1200 90 L0 90Z" fill="#fff"/>
    <path d="M0 30 Q300 110 620 55 T1200 8" fill="none" stroke="var(--orange)" stroke-width="5"/>
  </svg>
</section>

<section class="welcome">
  <h2 class="heading">Welcome to Look Round Eastvale</h2>
  <p>It is a long established fact that a reader will be distracted by the readable content of a page when looking at its layout. The point of using Lorem Ipsum is that it has a more-or-less normal distribution of letters, as opposed to using 'Content here, content here', making it look like readable English. Many desktop publishing packages and web page editors</p>
</section>

<section class="band category">
  <div class="band-bg" role="img" aria-label="Teal-toned view of open water with a distant lighthouse"></div>
  <h2 class="heading">Our Category</h2>
  <div class="category-grid">
    <a class="category-card" href="#"><div class="thumb" role="img" aria-label="Crowd at an outdoor gathering on grass" style="background:linear-gradient(135deg,#6f8f4f,#9aa7c0)"><svg class="play" viewBox="0 0 54 54"><circle cx="27" cy="27" r="26" fill="#fff"/><path d="M21 15l18 12-18 12z" fill="#444"/></svg></div><div class="label">People</div></a>
    <a class="category-card" href="#"><div class="thumb" role="img" aria-label="Person speaking indoors at an event" style="background:linear-gradient(135deg,#4a2f22,#8a5a3e)"><svg class="play" viewBox="0 0 54 54"><circle cx="27" cy="27" r="26" fill="#fff"/><path d="M21 15l18 12-18 12z" fill="#444"/></svg></div><div class="label">Events</div></a>
    <a class="category-card" href="#"><div class="thumb" role="img" aria-label="Vendor talking in a kitchen" style="background:linear-gradient(135deg,#5e5048,#9d8a7a)"><svg class="play" viewBox="0 0 54 54"><circle cx="27" cy="27" r="26" fill="#fff"/><path d="M21 15l18 12-18 12z" fill="#444"/></svg></div><div class="label">Meet the Vendors</div></a>
    <a class="category-card" href="#"><div class="thumb" role="img" aria-label="Colourful swirling painted artwork" style="background:linear-gradient(135deg,#c4541d,#e6a43a,#6b7f9c)"><svg class="play" viewBox="0 0 54 54"><circle cx="27" cy="27" r="26" fill="#fff"/><path d="M21 15l18 12-18 12z" fill="#444"/></svg></div><div class="label">Scenic Videos</div></a>
    <a class="category-card" href="#"><div class="thumb" role="img" aria-label="Street performers on a city sidewalk" style="background:linear-gradient(135deg,#7a7e84,#b9a89a)"><svg class="play" viewBox="0 0 54 54"><circle cx="27" cy="27" r="26" fill="#fff"/><path d="M21 15l18 12-18 12z" fill="#444"/></svg></div><div class="label">Performances</div></a>
    <a class="category-card" href="#"><div class="thumb" role="img" aria-label="Weathered stone garden statue" style="background:linear-gradient(135deg,#3e4a40,#8c9287)"><svg class="play" viewBox="0 0 54 54"><circle cx="27" cy="27" r="26" fill="#fff"/><path d="M21 15l18 12-18 12z" fill="#444"/></svg></div><div class="label">Lighter Side</div></a>
    <a class="category-card" href="#"><div class="thumb" role="img" aria-label="Painted wooden gallery sign" style="background:linear-gradient(135deg,#6f5c42,#c29a52)"><svg class="play" viewBox="0 0 54 54"><circle cx="27" cy="27" r="26" fill="#fff"/><path d="M21 15l18 12-18 12z" fill="#444"/></svg></div><div class="label">Dayinthesun</div></a>
    <a class="category-card" href="#"><div class="thumb" role="img" aria-label="Man being interviewed indoors" style="background:linear-gradient(135deg,#4b3a2c,#8a6a4b)"><svg class="play" viewBox="0 0 54 54"><circle cx="27" cy="27" r="26" fill="#fff"/><path d="M21 15l18 12-18 12z" fill="#444"/></svg></div><div class="label">Videos</div></a>
  </div>
</section>

<section class="recent">
  <h2 class="heading">Recent Uploads</h2>
  <div class="recent-grid">
    <article class="feature">
      <div class="thumb" role="img" aria-label="Old log cabin among green trees" style="background:linear-gradient(160deg,#5d7f45 0%,#7d6a52 55%,#4f7a3a 100%)"><svg class="play" viewBox="0 0 54 54"><circle cx="27" cy="27" r="25" fill="#fff" fill-opacity=".85"/><path d="M22 16l16 11-16 11z" fill="#333"/></svg></div>
      <h3>Recent Uploads</h3>
      <p>It is a long established fact that a reader will be distracted by readable</p>
    </article>
    <aside class="side-list">
      <div class="side-item"><div class="thumb" role="img" aria-label="Dancers in traditional costume" style="background:linear-gradient(135deg,#3d6b3a,#6b3d50)"><svg class="play" viewBox="0 0 54 54"><circle cx="27" cy="27" r="26" fill="#fff"/><path d="M21 15l18 12-18 12z" fill="#444"/></svg></div><div class="side-info"><h4>Navruz 2017</h4><p>It is a long established fact that a reader will be distracted by readable</p></div></div>
      <div class="side-item"><div class="thumb" role="img" aria-label="Farm stand under a blue sky" style="background:linear-gradient(160deg,#8fb3d6,#a77c5c)"><svg class="play" viewBox="0 0 54 54"><circle cx="27" cy="27" r="26" fill="#fff"/><path d="M21 15l18 12-18 12z" fill="#444"/></svg></div><div class="side-info"><h4>Green Gate Farm</h4><p>It is a long established fact that a reader will be distracted by readable</p></div></div>
      <div class="side-item"><div class="thumb" role="img" aria-label="Baskets of fresh berries" style="background:linear-gradient(135deg,#4f6b2c,#b08a2c,#6a2c3c)"><svg class="play" viewBox="0 0 54 54"><circle cx="27" cy="27" r="26" fill="#fff"/><path d="M21 15l18 12-18 12z" fill="#444"/></svg></div><div class="side-info"><h4>Dale's Berries</h4><p>It is a long established fact that a reader will be distracted by readable</p></div></div>
      <a class="view-more" href="#">View More »</a>
    </aside>
  </div>
</section>

<section class="band coming">
  <div class="band-bg" role="img" aria-label="Blue-toned view of a locomotive on railway tracks"></div>
  <h2 class="heading">Coming Soon....</h2>
  <div class="coming-grid">
    <div class="coming-card"><div class="thumb" role="img" aria-label="Vendor tent with cooking equipment" style="background:linear-gradient(135deg,#4a8a4a,#6a5a4a)"></div><div class="label">Toffee Kitchen</div></div>
    <div class="coming-card"><div class="thumb" role="img" aria-label="Table of handmade hats on display" style="background:linear-gradient(135deg,#7a4a3a,#c08a6a)"></div><div class="label">Brimworks Hats</div></div>
    <div class="coming-card"><div class="thumb" role="img" aria-label="Jar of salsa on a red table" style="background:linear-gradient(135deg,#a8301e,#d9a36a)"></div><div class="label">Marlow's Best Salsa</div></div>
    <div class="coming-card"><div class="thumb" role="img" aria-label="Large kettle of popcorn being stirred" style="background:linear-gradient(135deg,#5a4a3a,#c9a56a)"></div><div class="label">Kettle Corn</div></div>
  </div>
</section>

<section class="events">
  <h2 class="heading">Latest Events</h2>
  <div class="event-grid">
    <article class="event">
      <div class="thumb" role="img" aria-label="Dancers performing on an outdoor stage" style="background:linear-gradient(135deg,#3e5a34,#a0603c)"></div>
      <div class="event-meta"><span class="date">Dec 03</span><span class="count"><svg width="12" height="10" viewBox="0 0 12 10"><path d="M1 1h10v6H5l-3 2V7H1z" fill="none" stroke="#fff"/></svg>0</span></div>
      <h3>Ethnicfest 2017</h3>
      <p>It has survived not only five centuries, but also the leap into electronic typesetting.</p>
      <a class="more" href="#">Read More »</a>
    </article>
    <article class="event">
      <div class="thumb" role="img" aria-label="Kites flying over a grassy park" style="background:linear-gradient(180deg,#c9cdb8 0%,#a9b39a 55%,#4f6b33 100%)"></div>
      <div class="event-meta"><span class="date">Dec 03</span><span class="count"><svg width="12" height="10" viewBox="0 0 12 10"><path d="M1 1h10v6H5l-3 2V7H1z" fill="none" stroke="#fff"/></svg>0</span></div>
      <h3>Kite Festival</h3>
      <p>It has survived not only five centuries, but also the leap into electronic typesetting.</p>
      <a class="more" href="#">Read More »</a>
    </article>
    <article class="event">
      <div class="thumb" role="img" aria-label="Three women in costume at a waterfront park" style="background:linear-gradient(180deg,#b9c4cc 0%,#a07a7a 50%,#8a7a4a 100%)"></div>
      <div class="event-meta"><span class="date">Dec 03</span><span class="count"><svg width="12" height="10" viewBox="0 0 12 10"><path d="M1 1h10v6H5l-3 2V7H1z" fill="none" stroke="#fff"/></svg>0</span></div>
      <h3>Alice in Wonderland at Millstone Park</h3>
      <p>It has survived not only five centuries, but also the leap into electronic typesetting.</p>
      <a class="more" href="#">Read More »</a>
    </article>
  </div>
</section>

<footer class="site-footer">
  <nav class="footer-nav"><a href="#">About</a><span>|</span><a href="#">Privacy</a><span>|</span><a href="#">Terms</a><span>|</span><a href="#">Legal</a><span>|</span><a href="#">Contact</a></nav>
  <div class="social"><span></span><span></span><span></span><span></span><span></span><span></span></div>
  <p class="copyright">Copyright © 2017 &nbsp;All Rights Reserved</p>
</footer>

</body>
</html>
```